K.T.L Electrical Services Pty Ltd

Electrical contracting business. I have a base for the design which i like. The contact number needs to be changed to 0491736250 and the O made more solid and level with the rest of the letters. If you have any other ideas of what would make it better I'm happy to see them.

The back side to be written as dot points with the following:
- Residential & Commercial
- Maintenance
- PV & Battery servicing
- EV Chargers

```html
<!DOCTYPE html>
<html lang="en">
<head>
<meta charset="utf-8">
<title>K.T.L Electrical Services Pty Ltd – Business Cards</title>
<link rel="stylesheet" href="https://fonts.googleapis.com/css2?family=Lato:wght@400;700&family=Montserrat:wght@500;600;700;800&display=swap">
<style>
  :root{
    --backdrop:#2b2c2e;
    --card:#1e282b;
    --white:#ffffff;
    --slate:#8fa8a9;
    --amber:#f4b400;
    --text-soft:#e6ecec;
  }
  *{box-sizing:border-box;margin:0;padding:0}
  html,body{width:1200px;height:800px;overflow:hidden}
  body{
    background:var(--backdrop);
    display:flex;align-items:center;justify-content:center;gap:40px;
    font-family:"Lato",sans-serif;
  }
  .card{
    width:560px;height:320px;background:var(--card);
    position:relative;overflow:hidden;
    box-shadow:0 18px 40px rgba(0,0,0,.45);
  }

  /* Business name block */
  .business{display:flex;align-items:center;gap:16px}
  .business__mark{width:18px;height:18px;border-radius:50%;background:var(--slate);flex:none}
  .business__name{
    font-family:"Montserrat",sans-serif;font-weight:700;color:var(--white);
    text-transform:uppercase;letter-spacing:1.5px;line-height:1.2;
  }

  /* Front */
  .card--front{display:flex;flex-direction:column;justify-content:center;padding:0 48px}
  .card--front .business__name{font-size:30px}
  .services{
    margin-top:34px;font-family:"Montserrat",sans-serif;font-weight:500;
    font-size:13px;letter-spacing:1.2px;color:var(--text-soft);
    list-style:none;display:grid;grid-template-columns:auto auto;gap:9px 22px;
    justify-content:start;
  }
  .services li{display:flex;align-items:center;gap:7px;white-space:nowrap}
  .bolt{width:9px;height:14px;flex:none}

  /* Back */
  .card--back{display:flex;align-items:center;padding:0 30px}
  .card--back .business{width:200px;gap:10px;flex:none}
  .card--back .business__mark{width:12px;height:12px}
  .card--back .business__name{font-size:15px;letter-spacing:1px}
  .divider{width:1px;height:210px;background:var(--slate);margin:0 26px 0 18px;flex:none}
  .person{min-width:0}
  .person__name{
    font-family:"Montserrat",sans-serif;font-weight:800;font-size:23px;letter-spacing:1px;
    color:var(--slate);text-transform:uppercase;line-height:1;white-space:nowrap;
  }
  .person__role{color:var(--amber);font-size:15px;margin-top:7px}
  .contact{list-style:none;margin-top:18px;display:flex;flex-direction:column;gap:8px;color:var(--text-soft);font-size:13px}
  .contact li{display:flex;align-items:flex-start;gap:10px;white-space:nowrap}
  .icon{width:13px;height:13px;flex:none;margin-top:2px;fill:var(--slate)}
</style>
</head>
<body>

<section class="card card--front">
  <div class="business">
    <span class="business__mark"></span>
    <p class="business__name">K.T.L Electrical<br>Services Pty Ltd</p>
  </div>
  <ul class="services">
    <li><svg class="bolt" viewBox="0 0 9 14"><path d="M6 0 0 8h3.5L2.5 14 9 5.5H5.3z" fill="#f4b400"/></svg>RESIDENTIAL &amp; COMMERCIAL</li>
    <li><svg class="bolt" viewBox="0 0 9 14"><path d="M6 0 0 8h3.5L2.5 14 9 5.5H5.3z" fill="#f4b400"/></svg>MAINTENANCE</li>
    <li><svg class="bolt" viewBox="0 0 9 14"><path d="M6 0 0 8h3.5L2.5 14 9 5.5H5.3z" fill="#f4b400"/></svg>PV &amp; BATTERY SERVICING</li>
    <li><svg class="bolt" viewBox="0 0 9 14"><path d="M6 0 0 8h3.5L2.5 14 9 5.5H5.3z" fill="#f4b400"/></svg>EV CHARGERS</li>
  </ul>
</section>

<section class="card card--back">
  <div class="business">
    <span class="business__mark"></span>
    <p class="business__name">K.T.L Electrical<br>Services Pty Ltd</p>
  </div>
  <span class="divider"></span>
  <div class="person">
    <h1 class="person__name">Daniel Hartley</h1>
    <p class="person__role">Founder &amp; CEO</p>
    <ul class="contact">
      <li><svg class="icon" viewBox="0 0 12 12"><path d="M6 0a4 4 0 0 0-4 4c0 3 4 8 4 8s4-5 4-8a4 4 0 0 0-4-4zm0 5.5A1.5 1.5 0 1 1 6 2.5a1.5 1.5 0 0 1 0 3z"/></svg><span>423 Street Address Here, City<br>State &amp; Country, ZIP Code</span></li>
      <li><svg class="icon" viewBox="0 0 12 12"><path d="M2.5 0 4.5 2.6 3.4 4a7 7 0 0 0 4.6 4.6L9.4 7.5 12 9.5 10.5 12C5 12 0 7 0 1.5z"/></svg><span>0491736250</span></li>
      <li><svg class="icon" viewBox="0 0 12 12"><path d="M0 2h12v8H0zm1 1v.4l5 3.3 5-3.3V3z"/></svg><span>info@ktlelectricalservices.com</span></li>
      <li><svg class="icon" viewBox="0 0 12 12"><circle cx="6" cy="6" r="5.2" fill="none" stroke="#8fa8a9" stroke-width="1.4"/><path d="M.8 6h10.4M6 .8c-2.6 3-2.6 7.4 0 10.4M6 .8c2.6 3 2.6 7.4 0 10.4" fill="none" stroke="#8fa8a9" stroke-width="1"/></svg><span>ktlelectricalservices.com</span></li>
    </ul>
  </div>
</section>

</body>
</html>
```